Design for iOS app - Scanner App

We are developing an iOS app that is scanning receipts and mailing them to a predefined email address. The app should work more or less like TallySnap app (a short demo of the TallySnap app is available here: https://www.clipvault.example/watch?v=QmRtZpLwXkA).

We have prototyped the app in the link below:
http://app.wirepane.example/view/a71c3d9f2b8e40c6d5f18e27b9a4c3d0

NB!: Please do not follow the mockups literally, but the iOS Human Interface Guidelines!

The technical specifications and descriptions of the app's functionalities are available in the link below:
https://sheets.papyrdesk.example/document/d/9pQrx-TW2cNmbvJLhQ7dKzR4eWs-aY_3Hkv8Tfmn5xe/edit?usp=sharing

Requirements for the design:

- The design should be provided as PSD, where each page/section should be in its own PSD file OR all pages/sections should be represented as folder groups in a single PSD file.

- All graphical elements in the design should be delivered as single layers which can then be extracted from the PSD.

- All graphical elements (icons, graphical buttons, etc.) should be provided as vector objects in the PSD, so that they can be exported into different sizes without loss of quality (for responsiveness).

- The design should use either web safe fonts or Quorby Fonts.

Instructions for the design:

The design should have habitual user interface like ordinary iOS navigation stack, with navigation bar on the top and all other elements on the bottom. That means just to make the top bar in your app be more like iOS. Please follow the iOS Human Interface Guidelines, not the mockups literally .
FX: the e small elements in Dimensions screen like delete icons and active checkbox. In
https://devhub.orchardly.example/library/ios/documentation/UserExperience/Conceptual/MobileHIG/LayoutandAppearance.html#//ref/doc/uid/TP51208847-CH31-SW1
is described that interface elements should be at least 44x44 px - it's normal practice for all mobile development (iOS, android), so you should consider this too.

Please also provide an app icon and suggest a logo for the app.

Requirements
Must have
• Please make sure that the design is flat. Like iOS app, Pagefold, Quorby apps etc.
Nice to have
• The design could be somewhat like the design for Mindvale Pagefold(https://apps.orchardly.example/bg/app/mindvale-pagefold/id552719043?mt=8) without being too similar
Should not have
• 3D look

```html
<!DOCTYPE html>
<html lang="en">
<head>
<meta charset="utf-8">
<title>Scanner App – Camera Screen</title>
<link rel="stylesheet" href="https://fonts.googleapis.com/css2?family=Open+Sans:wght@400;600;700&display=swap">
<style>
  :root {
    --page-bg: #f2f2f2;
    --nav-dark: #0b2f4f;
    --nav-glass: rgba(22, 78, 122, 0.78);
    --nav-text: #ffffff;
    --accent-blue: #2a93dc;
    --ready-green: #39d67a;
    --button-bg: #dcdcdc;
    --button-text: #3d3d3d;
    --viewfinder-light: #f1c98c;
    --viewfinder-mid: #c98a4e;
    --viewfinder-dark: #6a3e22;
  }

  * { box-sizing: border-box; margin: 0; padding: 0; }

  html, body {
    width: 1200px;
    height: 900px;
    overflow: hidden;
    background: var(--page-bg);
    font-family: "Open Sans", Arial, sans-serif;
  }

  .app-screen {
    position: absolute;
    left: 375px;
    top: 50px;
    width: 450px;
    height: 800px;
    overflow: hidden;
    background: var(--viewfinder-mid);
  }

  .camera-viewfinder {
    position: absolute;
    inset: 0;
    background:
      radial-gradient(ellipse at 55% 18%, var(--viewfinder-light) 0%, rgba(241,201,140,0) 60%),
      linear-gradient(180deg, #e8b677 0%, #cf9455 45%, #9c5d33 75%, var(--viewfinder-dark) 100%);
  }

  .nav-bar {
    position: absolute;
    left: 0; top: 0; right: 0;
    color: var(--nav-text);
  }

  .nav-bar__top {
    height: 34px;
    background: var(--nav-dark);
    display: flex;
    justify-content: flex-end;
    align-items: center;
    gap: 10px;
    padding-right: 14px;
  }

  .nav-bar__main {
    height: 58px;
    background: var(--nav-glass);
    position: relative;
    display: flex;
    align-items: center;
    justify-content: center;
  }

  .nav-bar__title {
    font-size: 17px;
    font-weight: 400;
    letter-spacing: 0.5px;
  }

  .nav-bar__info {
    position: absolute;
    left: 12px;
    top: 50%;
    transform: translateY(-50%);
    width: 26px;
    height: 26px;
  }

  .icon { display: block; }

  .scan-button {
    position: absolute;
    left: 50%;
    top: 200px;
    transform: translateX(-50%);
    width: 196px;
    height: 196px;
    border-radius: 50%;
    background: var(--accent-blue);
    border: none;
    color: #ffffff;
    font-family: "Open Sans", Arial, sans-serif;
    font-size: 38px;
    font-weight: 700;
    letter-spacing: 1px;
  }

  .status-ready {
    position: absolute;
    left: 176px;
    bottom: 112px;
    color: var(--ready-green);
    font-size: 19px;
    font-weight: 600;
    letter-spacing: 0.5px;
  }

  .queue-bar {
    position: absolute;
    left: 14px;
    right: 14px;
    bottom: 22px;
    display: flex;
    gap: 14px;
  }

  .queue-button {
    flex: 1;
    height: 66px;
    border: none;
    border-radius: 10px;
    background: var(--button-bg);
    color: var(--button-text);
    font-family: "Open Sans", Arial, sans-serif;
    font-size: 17px;
    font-weight: 700;
    letter-spacing: 0.3px;
  }
</style>
</head>
<body>
  <main class="app-screen">
    <div class="camera-viewfinder" role="img" aria-label="Live camera preview showing a warmly lit living room with sofas, a rug and a coffee table"></div>

    <header class="nav-bar">
      <div class="nav-bar__top">
        <svg class="icon icon--flash" width="14" height="22" viewBox="0 0 14 22" aria-label="Flash">
          <path d="M8 0 L1 12 H6 L4 22 L13 8 H8 Z" fill="var(--accent-blue)"/>
        </svg>
        <svg class="icon icon--settings" width="24" height="24" viewBox="0 0 24 24" aria-label="Settings">
          <g fill="var(--accent-blue)">
            <circle cx="12" cy="12" r="7.5"/>
            <rect x="10" y="1" width="4" height="22" rx="1"/>
            <rect x="1" y="10" width="22" height="4" rx="1"/>
            <rect x="10" y="1" width="4" height="22" rx="1" transform="rotate(45 12 12)"/>
            <rect x="10" y="1" width="4" height="22" rx="1" transform="rotate(-45 12 12)"/>
          </g>
          <circle cx="12" cy="12" r="3.4" fill="var(--nav-dark)"/>
        </svg>
      </div>
      <div class="nav-bar__main">
        <svg class="nav-bar__info" viewBox="0 0 26 26" aria-label="Info">
          <circle cx="13" cy="13" r="12" fill="#d8d8d8"/>
          <circle cx="13" cy="7.5" r="1.8" fill="#333"/>
          <rect x="11.3" y="10.5" width="3.4" height="9" rx="1" fill="#333"/>
        </svg>
        <h1 class="nav-bar__title">SCANNER APP</h1>
      </div>
    </header>

    <button class="scan-button" type="button">SCAN</button>

    <p class="status-ready">READY</p>

    <nav class="queue-bar">
      <button class="queue-button queue-button--pending" type="button">PENDING (5)</button>
      <button class="queue-button queue-button--sent" type="button">SENT (3)</button>
    </nav>
  </main>
</body>
</html>
```